Insurance Agency Flyer
8.5 x 11 Double Sided Full Color
Bluelanem your draft #10 is good except that due to trademark issues we must display the insurance company logos across the bottom on a white background only. The overall design is sleek but the blue background under the logos would be a deal breaker. I like the idea of using a house and car also but not that particular house, car and people. Good examples of the kinds of photos we are seeking are those seen in draft #5 and draft #6
@PH - please check your private message on right top once you login.
Thanks
Ravenwood, draft #3 is good. Can you try changing the font color and/or size and/or style of certain words in the "why are you paying so much for auto insurance" line? For example in draft #2, auto insurance stands out more because it is in a different color. I would be curious to see what other options there are to make those words stand out.
Tobel, I like draft #2 however can you make the following modifications:
1. Please note that while we are allowed to use the "Lakemount" logo we can't use their symbols for the Auto, home, motorcycle... etc. Could you replace those symbols with something similar?
2. The CMQ logo should be placed somewhere else as this is not one of our insurance but rather an organization we belong to (for example in draft #1 it is listed on the bottom right).
3. Also, could our phone number be more pronounced somewhere?
4. And finally, I like the overall clean layout but not crazy about that particular guy and car. Any other options?
Ravnewood, I really like draft #1. I would be inetrested to see how it might look if the auto, home, motorcycle... icons were also across the very top of page 1? Also, Is there a way to put more emphasis on the words "auto insurance" justs o that they stand out more, maybe more than the "Paying so Much".

```html
<!DOCTYPE html>
<html lang="en">
<head>
<meta charset="utf-8">
<title>KRV Coverage Agency – Auto Insurance Flyer</title>
<link href="https://fonts.googleapis.com/css2?family=Arimo:wght@400;700&family=Tinos:wght@400;700&display=swap" rel="stylesheet">
<style>
:root{
  --navy:#0d3f73;
  --blue:#1c5d9a;
  --sky:#3f9ad8;
  --orange:#f39a1e;
  --ink:#3b3b3b;
  --grey:#6a6a6a;
  --line:#c9d3de;
  --paper:#ffffff;
  --stage:#e9ecef;
}
*{box-sizing:border-box;margin:0;padding:0}
html,body{width:1200px;height:799px;overflow:hidden;background:var(--stage)}
.canvas{position:relative;width:1200px;height:799px}
.page{position:absolute;top:64px;width:518px;height:672px;background:var(--paper);overflow:hidden;box-shadow:0 2px 8px rgba(0,0,0,.18)}
.page--front{left:72px}
.page--back{left:631px}
.abs{position:absolute}
.sans{font-family:'Arimo',Arial,sans-serif}
.serif{font-family:'Tinos','Times New Roman',serif}
.accent{color:var(--orange)}

/* front */
.hero-band{left:0;top:0;width:518px;height:172px;background:linear-gradient(180deg,var(--navy),var(--blue))}
.headline{left:0;width:518px;text-align:center;color:#fff;font-family:'Arimo',Arial,sans-serif}
.headline--one{top:24px;font-size:29px}
.headline--two{top:60px;font-size:29px}
.headline--three{top:112px;font-size:26px}
.headline b{font-weight:700}
.keys-photo{left:120px;top:186px;width:270px;height:150px;border-radius:40px 90px 30px 60px;background:radial-gradient(ellipse at 40% 40%,#5a5f66,#1c1f24 70%,#c8ccd1 100%)}
.site-small{right:24px;top:182px;font-size:10px;color:var(--grey)}
.swoosh{left:0;top:318px}
.how-title{right:28px;top:384px;font-size:25px;color:var(--blue);font-family:'Arimo',Arial,sans-serif}
.benefit-box{left:92px;top:420px;width:400px;height:122px;border:1px solid var(--line);border-radius:6px;background:linear-gradient(180deg,#fff,#f1f4f8)}
.benefit-list{list-style:none;text-align:center;padding-top:6px;font-family:'Tinos','Times New Roman',serif;font-size:14.5px;line-height:18px;color:var(--ink)}
.brand{display:flex;align-items:center;gap:8px;font-family:'Tinos','Times New Roman',serif;font-weight:700;color:var(--navy);white-space:nowrap}
.brand-mark{width:22px;height:22px;background:var(--navy);flex:none}
.brand--front{left:0;width:518px;top:560px;justify-content:center;font-size:26px}
.address-line{left:0;width:518px;top:616px;text-align:center;font-size:10.5px;color:var(--ink)}
.partner-strip{left:0;bottom:0;width:518px;height:34px;border-top:3px solid var(--blue);display:flex;align-items:center;justify-content:space-around;padding:0 10px;background:var(--paper)}
.partner{font-family:'Arimo',Arial,sans-serif;font-weight:700;font-size:10px;color:var(--navy)}
.badge{width:16px;height:20px;background:var(--navy);border-radius:2px}

/* back */
.call-title{left:0;width:518px;text-align:center;font-family:'Tinos','Times New Roman',serif;color:var(--grey);font-size:25px}
.call-title--one{top:20px}
.call-title--two{top:50px}
.phone{left:0;width:518px;top:88px;text-align:center;font-family:'Arimo',Arial,sans-serif;font-size:36px;color:var(--sky)}
.office{left:0;width:518px;top:140px;text-align:center;font-family:'Tinos','Times New Roman',serif;font-weight:700;font-size:19px;line-height:25px;color:var(--ink);font-style:normal}
.save-line{left:0;width:518px;top:220px;text-align:center;font-family:'Tinos','Times New Roman',serif;font-size:21px;color:var(--grey)}
.back-band{left:0;top:270px}
.claims-badge{left:42px;top:272px;width:92px;height:92px;border-radius:50%;background:var(--blue);border:4px solid #fff;box-shadow:0 0 0 2px var(--sky);color:#fff;text-align:center;font-family:'Arimo',Arial,sans-serif}
.claims-badge .big{display:block;margin-top:18px;font-size:26px;font-weight:700}
.claims-badge .small{display:block;font-size:10px;line-height:11px}
.perk-list{left:156px;top:274px;list-style:none;font-family:'Tinos','Times New Roman',serif;font-size:13px;line-height:18px;color:var(--ink)}
.keychain-photo{left:56px;top:378px;width:150px;height:56px;border-radius:28px 10px 28px 10px;background:linear-gradient(120deg,#c9ccd0,#f2f2f2 40%,#c8271f 70%,#8d1510)}
.logo-card{left:382px;top:512px;width:122px;height:50px;background:#fff;border-radius:3px;display:flex;align-items:center;justify-content:center}
.brand--back{font-size:15px;gap:5px}
.brand--back .brand-mark{width:14px;height:14px}
.site-back{right:16px;top:574px;font-family:'Tinos','Times New Roman',serif;font-size:15px;color:#fff}
</style>
</head>
<body>
<main class="canvas">

  <section class="page page--front">
    <div class="abs hero-band"></div>
    <h1 class="abs headline headline--one">Why are you <b>paying so much</b></h1>
    <p class="abs headline headline--two">for <b class="accent">auto insurance?</b></p>
    <p class="abs headline headline--three">Let <b>KRV</b> lower your auto <b class="accent">insurance bill!</b></p>

    <div class="abs keys-photo" role="img" aria-label="Photo of a car key and remote fob"></div>
    <span class="abs site-small serif">www.krvcoverage.com</span>
    <svg class="abs swoosh" width="518" height="80" viewBox="0 0 518 80">
      <path d="M0 40 C140 70 330 10 518 30 L518 80 L0 80 Z" fill="#e6eef6"/>
      <path d="M0 52 C160 80 340 24 518 40" stroke="#1c5d9a" stroke-width="6" fill="none"/>
      <path d="M0 62 C170 86 350 34 518 52" stroke="#3f9ad8" stroke-width="2" fill="none"/>
    </svg>

    <h2 class="abs how-title">How does <b>KRV</b> do it?</h2>
    <div class="abs benefit-box">
      <ul class="benefit-list">
        <li>Find discounts you may be missing</li>
        <li>Comparison shop with multiple companies on your behalf</li>
        <li>Package policies for even more savings</li>
        <li>Find ways to reduce or eliminate fees</li>
        <li>KRV has NO agency fees</li>
        <li>Customize a policy just for you</li>
      </ul>
    </div>

    <div class="abs brand brand--front"><span class="brand-mark"></span>KRV Coverage</div>
    <p class="abs address-line serif">KRV Coverage Agency, 2210-B Harlow Creek Rd., Fairbrook, NC 28199 | www.krvcoverage.com</p>

    <footer class="abs partner-strip">
      <span class="partner">Northfield</span>
      <span class="partner">Oakline Auto &amp; Home</span>
      <span class="partner">Lakemount</span>
      <span class="badge"></span>
      <span class="partner">Vantor</span>
      <span class="partner">Stonebridge</span>
    </footer>
  </section>

  <section class="page page--back">
    <h2 class="abs call-title call-title--one">Call KRV before paying your</h2>
    <p class="abs call-title call-title--two">next <span class="accent">insurance bill</span></p>
    <p class="abs phone">(555) 013-2270</p>
    <address class="abs office">KRV Coverage Agency,<br>2210-B Harlow Creek Rd.,<br>Fairbrook, NC 28199</address>
    <p class="abs save-line">Save money without cutting coverage or service</p>

    <svg class="abs back-band" width="518" height="368" viewBox="0 0 518 368">
      <defs>
        <linearGradient id="bandFill" x1="0" y1="0" x2="0" y2="1">
          <stop offset="0" stop-color="#1c5d9a"/>
          <stop offset="1" stop-color="#0d3f73"/>
        </linearGradient>
      </defs>
      <path d="M0 40 C180 10 360 70 518 60 L518 368 L0 368 Z" fill="#eef2f6"/>
      <path d="M0 150 C200 110 360 170 518 120 L518 368 L0 368 Z" fill="url(#bandFill)"/>
      <path d="M0 150 C200 110 360 170 518 120" stroke="#3f9ad8" stroke-width="3" fill="none"/>
      <rect x="0" y="334" width="518" height="34" fill="#ffffff"/>
      <rect x="0" y="331" width="518" height="3" fill="#1c5d9a"/>
    </svg>

    <div class="abs claims-badge"><span class="big">24/7</span><span class="small">Claims<br>Services</span></div>
    <ul class="abs perk-list">
      <li>Local Agent</li>
      <li>Variety of discounts available</li>
      <li>Guaranteed claims repairs</li>
      <li>A-Rated CMQ Accredited Business</li>
      <li>Friendly knowledgeable agents</li>
    </ul>
    <div class="abs keychain-photo" role="img" aria-label="Photo of a key with a red insurance tag"></div>

    <div class="abs logo-card"><div class="brand brand--back"><span class="brand-mark"></span>KRV Coverage</div></div>
    <span class="abs site-back">www.krvcoverage.com</span>

    <footer class="abs partner-strip">
      <span class="partner">Northfield</span>
      <span class="partner">Oakline Auto &amp; Home</span>
      <span class="partner">Lakemount</span>
      <span class="badge"></span>
      <span class="partner">Vantor</span>
      <span class="partner">Stonebridge</span>
    </footer>
  </section>

</main>
</body>
</html>
```